Math Help Website Needs New Design

Looking to refresh the design of my existing site (brightsumguide.net) to be easier on the eyes. I am fully capable of doing the HTML coding and have for years, but I don't have the eye for good design, colors, layout, and fonts. This is where I need help!

I need both a new design scheme and a new logo that matches. The overall functionality will be the same as the existing site, and should not be unrecognizable.

Target Market(s)

It should appeal to students (age 13-22) and their parents, so it should NOT be childish in appearance, nor should it be corporate.

Requirements
Must have
• Should be simple, easy-to-navigate, and neither childish nor corporate. I am looking for a design for both the homepage and a similar "content" page. Simple, bold colors are preferred. A logo should be prominent at the top, with a search bar nearby. Below that I need a similar navigational area like I already have. Then, I need about 200px wide ad space on the left of the main body area.

```html
<!DOCTYPE html>
<html lang="en">
<head>
<meta charset="utf-8">
<title>Bright Sum Guide</title>
<link href="https://fonts.googleapis.com/css2?family=PT+Sans:wght@400;700&family=Oswald:wght@500&display=swap" rel="stylesheet">
<style>
:root{
  --blue:#2a97dd;--blue-dark:#1e7fc4;--navy:#2d5395;--orange:#f68b1f;--orange-dark:#e07410;
  --purple:#5b4b9e;--green:#6cb51f;--ink:#333;--muted:#666;--line:#e3e3e3;--hero:#f2f2f2;--foot:#3b3b3b;
}
*{box-sizing:border-box;margin:0;padding:0}
html,body{width:822px;height:1200px;overflow:hidden}
body{position:relative;background:#fff;font-family:"PT Sans",sans-serif;color:var(--ink);font-size:9px}
.abs{position:absolute}
.topband{left:0;top:0;width:822px;height:200px;background:linear-gradient(#1f8cd6,#39a5e6)}
.brand{left:44px;top:30px;display:flex;align-items:center;gap:8px;color:#fff;font-weight:700;font-size:24px}
.brand i{display:block;width:20px;height:20px;border-radius:50%;background:#fff}
.search{left:262px;top:30px;width:316px;height:46px;background:rgba(255,255,255,.18);border-radius:3px}
.search .field{position:absolute;left:12px;top:10px;width:268px;height:25px;background:#fff;border-radius:2px 0 0 2px;font-style:italic;color:#999;font-size:9.5px;padding:7px 10px}
.search .go{position:absolute;left:280px;top:10px;width:26px;height:25px;background:#1b5f94;color:#fff;font-size:11px;text-align:center;line-height:25px}
.social{left:691px;top:61px;display:flex;gap:3px}
.social span{width:17px;height:17px;border-radius:50%;background:#fff}
.nav{left:46px;top:90px;width:730px;height:38px;background:linear-gradient(#f79a2e,var(--orange-dark));display:flex;align-items:center;padding-left:20px}
.nav a{color:#fff;text-decoration:none;font-size:12.5px;padding:0 16px;border-right:1px solid rgba(255,255,255,.6);line-height:15px}
.nav a:last-child{border:0}
.hero{left:46px;top:128px;width:730px;height:242px;background:var(--hero)}
.hero-photo{position:absolute;right:0;top:0;width:358px;height:242px;background:linear-gradient(100deg,#f4f4f4,#e9e4e6 40%,#f6f6f6)}
.hero h1{position:absolute;left:42px;top:36px;font-size:24px;font-weight:400;color:#2f4e84}
.hero h2{position:absolute;left:43px;top:66px;font-size:16px;font-weight:400;color:var(--orange)}
.hero p{position:absolute;left:42px;top:90px;width:300px;font-size:9px;line-height:17px;color:var(--muted)}
.btn{position:absolute;top:148px;height:23px;color:#fff;font-family:"Oswald",sans-serif;font-size:10px;text-align:center;line-height:23px;border-radius:2px}
.btn.learn{left:42px;width:92px;background:var(--purple)}
.btn.join{left:141px;width:91px;background:var(--orange)}
.dots{position:absolute;left:42px;top:188px;display:flex;gap:2px}
.dots span{width:5px;height:5px;border-radius:50%;background:#ccc}
.dots span:first-child{background:#888}
.sidebox{left:47px;width:143px;border:1px solid var(--line);background:#fff}
.side-head{height:31px;color:#fff;font-size:12.5px;padding:7px 18px}
.side-head.blue{background:linear-gradient(#3569b0,var(--navy))}
.side-head.green{background:linear-gradient(#7fc42d,#5aa314)}
.sheet li{list-style:none;margin:0 12px;border-bottom:1px solid #f0f0f0;height:21.6px;line-height:21.6px;font-size:9px;color:var(--navy);padding-left:18px;position:relative}
.sheet li::before{content:"›";position:absolute;left:6px;color:#999}
.sheet li:last-child{border:0}
.tab-pill{position:absolute;left:77px;width:57px;height:16px;background:var(--navy);color:#fff;font-size:8.5px;text-align:center;line-height:17px;border-radius:14px 14px 0 0}
.apple{left:47px;top:581px;width:143px;height:142px;background:linear-gradient(135deg,#3f6a3a,#2f5a2c 60%,#4c7d3c)}
.help-item{display:flex;gap:10px;padding:0 10px 0 12px;margin-top:10px}
.help-item i{flex:none;width:24px;height:24px;background:#b9b9b9;border:1px solid #ddd}
.help-item p{font-size:7.5px;line-height:13px;color:var(--muted)}
.main h3{font-size:16px;font-weight:700;color:#333}
.lead{font-size:8.6px;line-height:14.4px;font-weight:700;color:#555}
.body{font-size:8.6px;line-height:14.4px;color:var(--muted)}
.card{top:545px;width:178px;height:190px;border:1px solid var(--line);background:#fff}
.card-head{height:30px;background:linear-gradient(#f8992c,var(--orange-dark));color:#fff;font-size:12.5px;padding:6px 16px}
.card .txt{padding:13px 14px 0;font-size:8.6px;line-height:14px;color:var(--muted)}
.card ul{padding:10px 14px 0}
.card li{list-style:none;font-size:7.6px;color:#333;height:18px;padding-left:14px;position:relative}
.card li::before{content:"";position:absolute;left:0;top:1px;width:9px;height:9px;border-radius:50%;background:#e6e6e6}
.card li::after{content:"";position:absolute;left:3.5px;top:3.5px;border:2px solid transparent;border-left:3px solid #555}
.tool{left:213px;top:756px;width:561px;height:363px;border:1px solid var(--line);background:#fff}
.tabs{height:32px;background:linear-gradient(#3467b0,var(--navy));display:flex;align-items:flex-end;padding-left:6px;border-radius:3px 3px 0 0}
.tabs span{color:#fff;font-size:10px;padding:0 13px;height:32px;line-height:32px}
.tabs span.on{background:#fff;color:var(--navy);font-size:12.5px;height:32px;font-weight:700;border-radius:3px 3px 0 0;margin-top:-4px}
.sym{position:absolute;left:26px;display:flex;gap:0}
.sym span{width:46px;text-align:center;font-size:14px;color:#222}
.label{position:absolute;font-size:11px;font-weight:700;color:var(--navy)}
.problem{left:118px;top:124px;width:374px;height:46px;background:#fdf4e3;border:1px dashed #e2a23c}
.examples{left:118px;top:186px;width:376px;height:84px;border:1px solid #d7d7d7;overflow:hidden;padding:4px 20px 0 6px}
.examples div{font-size:9px;color:#3a62a8;height:16px;display:flex;align-items:center;gap:4px}
.examples div::before{content:"+";width:9px;height:9px;border:1px solid #555;font-size:8px;line-height:7px;text-align:center;color:#333}
.scroll{position:absolute;right:2px;top:2px;width:14px;height:78px;background:#f1f4fa;border-left:1px solid #dde}
.select{left:118px;top:289px;width:376px;height:18px;background:#fdf4e3;border:1px solid #d8cfc0}
.select::after{content:"";position:absolute;right:3px;top:3px;width:11px;height:10px;background:#c8d6ee}
.answer{left:117px;top:318px;width:88px;height:27px;background:var(--orange);color:#fff;font-size:12.5px;font-weight:700;text-align:center;line-height:27px}
.footer{left:0;top:1140px;width:822px;height:60px;background:var(--foot);border-top:4px solid #e2e2e2;color:#eee;font-size:9px}
.footer .copy{position:absolute;left:50px;top:24px}
.footer .links{position:absolute;right:50px;top:24px}
</style>
</head>
<body>
<div class="abs topband"></div>
<div class="abs brand"><i></i>Bright Sum Guide</div>
<div class="abs search"><div class="field">type here for Search now..</div><div class="go">Go</div></div>
<div class="abs social"><span></span><span></span><span></span><span></span></div>
<nav class="abs nav"><a>Home</a><a>Algebra</a><a>Geometry</a><a>Trig</a><a>Calculus</a><a>Statistics</a><a>More Subjects</a><a>Message Board</a></nav>

<section class="abs hero">
  <div class="hero-photo" role="img" aria-label="Teacher writing math diagrams on a whiteboard"></div>
  <h1>Bright Sum Guide to All Students</h1>
  <h2>We offers Best Coaching &amp; Training</h2>
  <p>Pellentesque habitant morbi tristique senectus et netus et malesuada fames ac turpis egestas. Cras id elit. Integer quis urna. Ut ante enim, dapibus malesuada, fringilla eu, condimentum quis, tellus.</p>
  <div class="btn learn">LEARN MORE</div><div class="btn join">JOIN US NOW</div>
  <div class="dots"><span></span><span></span><span></span><span></span></div>
</section>

<aside class="abs sidebox" style="top:382px;height:188px">
  <div class="side-head blue">Worksheet</div>
  <ul class="sheet" style="margin-top:10px"><li>Maths</li><li>Physics</li><li>Chemistry</li><li>Biology</li><li>English</li><li>SST</li></ul>
  <div class="tab-pill" style="top:171px">View</div>
</aside>
<div class="abs apple" role="img" aria-label="Green apple held in front of a chalkboard with a triangle sketch"></div>
<aside class="abs sidebox" style="top:732px;height:387px">
  <div class="side-head green">Get Live Help</div>
  <div class="help-item"><i></i><p>Nunc tempus felis vitae urna. porttitor, neque at</p></div>
  <div class="help-item" style="margin-top:14px"><i></i><p>Maecenas at justo id velit placerat molestie.</p></div>
  <div class="help-item" style="margin-top:14px"><i></i><p>Aenean porttitor eros vel dolor. Donec convallis pede venenatis nibh. Duis quam. Nam eget lacus. Aliquam erat volutpat. Quisque congue leo.</p></div>
  <div class="help-item" style="margin-top:14px"><i></i><p>Mauris vel lacus vitae felis vestibulum volutpat. Etiam est nunc, venenatis in, tristique eu, imperdiet ac, nisl. Cum sociis natoque penatibus et magnis</p></div>
  <div class="help-item" style="margin-top:14px"><i></i><p>Aenean porttitor eros vel dolor. Donec convallis pede venenatis nibh.</p></div>
  <div class="tab-pill" style="top:370px">more</div>
</aside>

<main class="abs main" style="left:214px;top:388px;width:560px">
  <h3>Welcome to Bright Sum Guide Mainpage</h3>
  <p class="lead" style="margin-top:6px">Duis tincidunt lectus quis dui viverra vestibulum. Suspendisse vulputate aliquam dui. Nulla elementum dui ut augue. Aliquam vehicula mi at mauris. Maecenas placerat, nisl at consequat rhoncus, sem nunc gravida justo, quis eleifend arcu velit quis lacus.</p>
  <p class="body" style="margin-top:6px">Morbi magna magna, tincidunt a, mattis non, imperdiet vitae, tellus. Sed odio est, auctor ac, sollicitudin in, consequat vitae, orci. Fusce id felis. Vivamus sollicitudin metus eget eros. Pellentesque habitant morbi tristique senectus et netus et malesuada fames ac turpis egestas. In posuere felis nec tortor. Pellentesque faucibus. Ut accumsan ultricies elit. Maecenas at justo id velit placerat molestie. Donec dictum lectus non odio. Cras a ante vitae enim iaculis aliquam. Mauris nunc quam, venenatis nec, euismod sit amet, egestas placerat, est. Pellentesque habitant morbi tristique senectus et netus et malesuada fames ac turpis egestas. Cras id elit. Integer quis urna.</p>
</main>

<div class="abs card" style="left:212px"><div class="card-head">What's New?</div>
  <p class="txt">Mauris vel lacus vitae felis vestibulum volutpat. Etiam est nunc, venenatis in, tristique eu, imperdiet ac</p>
  <ul><li>Multiplying Polynomials</li><li>Derivative of an Inverse Function</li><li>Derivatives of Logs and Exps</li><li>Differentiating Trig Functions</li></ul></div>
<div class="abs card" style="left:404px"><div class="card-head">Math Lessons</div>
  <p class="txt">Mauris vel lacus vitae felis vestibulum volutpat. Etiam est nunc.</p>
  <ul><li>Algebra &amp; Geometry</li><li>Trignometry</li><li>Calcuius</li><li>Statistics</li><li>Sports Math</li><li>Calculators</li></ul></div>
<div class="abs card" style="left:596px"><div class="card-head">How We Teach</div>
  <p class="txt" style="font-weight:700;color:#444">Nunc tempus felis vitae urna. Vivamus neque at volutpat rutrum</p>
  <p class="txt" style="padding-top:4px;font-size:8px">Purus nisi eleifend libero, a tempus libero lectus feugiat felis. Morbi diam mauris, viverra in, gravida eu, mattis in, ante. Morbi eget arcu. Morbi porta, libero id ullamcorper nonummy, nibh ligula pulvinar metus, eget consectetuer augue nisi quis lacus.</p></div>

<section class="abs tool">
  <div class="tabs"><span>Basic Math</span><span>Pre-Algebra</span><span class="on">Algebra</span><span>Trignometry</span><span>Precalculus</span><span>Calculus</span><span>Statistics</span></div>
  <div class="sym" style="top:50px">
    <span><svg width="22" height="14"><path d="M4 1Q1 7 4 13M18 1Q21 7 18 13" stroke="#222" fill="none"/><rect x="6" y="3" width="10" height="8" fill="#8fb0e6" stroke="#335"/></svg></span>
    <span><svg width="22" height="14"><path d="M5 1H3V13H5M17 1H19V13H17" stroke="#222" fill="none" stroke-width="1.5"/><rect x="6" y="3" width="10" height="8" fill="#8fb0e6" stroke="#335"/></svg></span>
    <span><svg width="22" height="14"><path d="M3 1V13M19 1V13" stroke="#222" stroke-width="1.5"/><rect x="6" y="3" width="10" height="8" fill="#8fb0e6" stroke="#335"/></svg></span>
    <span><svg width="22" height="18"><rect x="6" y="1" width="10" height="6" fill="#8fb0e6" stroke="#335"/><path d="M3 9H19" stroke="#222"/><rect x="6" y="11" width="10" height="6" fill="#8fb0e6" stroke="#335"/></svg></span>
    <span><svg width="22" height="16"><rect x="4" y="4" width="10" height="11" fill="#8fb0e6" stroke="#335"/><rect x="15" y="1" width="5" height="5" fill="#8fb0e6" stroke="#335"/></svg></span>
    <span><svg width="22" height="16"><rect x="4" y="1" width="10" height="11" fill="#8fb0e6" stroke="#335"/><rect x="15" y="10" width="5" height="5" fill="#8fb0e6" stroke="#335"/></svg></span>
    <span><svg width="24" height="16"><path d="M1 9L3 8L6 15L9 1H23" stroke="#222" fill="none"/><rect x="10" y="4" width="11" height="9" fill="#8fb0e6" stroke="#335"/></svg></span>
    <span><svg width="24" height="16"><rect x="1" y="1" width="4" height="4" fill="#8fb0e6" stroke="#335"/><path d="M1 9L3 8L6 15L9 1H23" stroke="#222" fill="none"/><rect x="10" y="4" width="11" height="9" fill="#8fb0e6" stroke="#335"/></svg></span>
    <span><svg width="24" height="22"><path d="M3 1H1V21H3M21 1H23V21H21" stroke="#222" fill="none"/><g fill="#8fb0e6" stroke="#335"><rect x="4" y="3" width="4" height="4"/><rect x="10" y="3" width="4" height="4"/><rect x="16" y="3" width="4" height="4"/><rect x="4" y="9" width="4" height="4"/><rect x="10" y="9" width="4" height="4"/><rect x="16" y="9" width="4" height="4"/><rect x="4" y="15" width="4" height="4"/><rect x="10" y="15" width="4" height="4"/><rect x="16" y="15" width="4" height="4"/></g></svg></span>
    <span><svg width="26" height="14"><path d="M3 1Q0 7 3 13M23 1Q26 7 23 13" stroke="#222" fill="none"/><rect x="4" y="3" width="7" height="8" fill="#8fb0e6" stroke="#335"/><rect x="15" y="3" width="7" height="8" fill="#8fb0e6" stroke="#335"/><circle cx="13" cy="11" r="1" fill="#222"/></svg></span>
  </div>
  <div class="sym" style="top:74px;font-family:Georgia,serif">
    <span>f(x)</span><span>ln</span><span>log</span><span>log<sub style="display:inline-block;width:5px;height:5px;background:#8fb0e6;border:1px solid #335"></sub></span><span>≥</span><span>≤</span><span>÷</span><span><i>π</i></span><span>∪</span><span>∩</span>
  </div>
  <div class="label" style="left:31px;top:126px">Enter Problem:</div>
  <div class="abs problem"></div>
  <div class="label" style="left:31px;top:183px">Examples:</div>
  <div class="abs examples">
    <div>Absolute Value Expressions and Equations</div><div>Radical Expressions and Equations</div><div>Rational Expressions and Equations</div><div>Systems of Equations</div><div>Quadratic Equations</div>
    <span class="scroll"></span>
  </div>
  <div class="label" style="left:37px;top:290px">Select Topic</div>
  <div class="abs select"></div>
  <div class="abs answer">Answer</div>
</section>

<footer class="abs footer">
  <span class="copy">Copyright © 2012 Company Name. All righ reserved.&nbsp; Term of Use.</span>
  <span class="links">Home / Algebra / Geometry / Trig / Calculus / Statistics / More Subjects / Message Board</span>
</footer>
</body>
</html>
```